We need an attractive, simple & modern / Aussie Design of BusinessCard using the existing company Logo.
Our company is located in Perth, WA, Australia.
The Company name is Kestrel Hollow Construction & Maintenance
Name on the card is Doran Pellick
Designation is Managing Director
Building Registration BC584317
M: 0438 715 362
E: kestrelhollowbuild@mailpost.example

Our main tasks are Building new homes, medical centers, mixed use. Renovations & Maintenance.

Slogan: Let Quality Meets Your Budget (We are open if you please suggest something more attractive within same concept)

Target Market(s)

Individuals to build or renovate homes, Doctors and dentists to build, renovate, fit off clinics and medical centres, Schools & real estate offices for maintenance contracts.

Industry/Entity Type

Construction

Contact Information for Business Card

To contain company name, logo, person name and contact details, building registration detail, slogan and to give brief on our services

Colors

Designer to choose colors to be used in the design.

Requirements
Must have
• To have attractive design. And contain company name, logo, person name, designation and contact details, building registration detail, slogan and to give brief on our services.
• Elegant and Simple Style.
Nice to have
• Modern Aussie style.
Should not have
• Should not be too much busy or complicated.

```html
<!DOCTYPE html>
<html lang="en">
<head>
<meta charset="utf-8">
<title>Kestrel Hollow Construction &amp; Maintenance – Business Card</title>
<link rel="stylesheet" href="https://fonts.googleapis.com/css2?family=Open+Sans:wght@400;600;700&display=swap">
<style>
  :root {
    --backdrop: #3e9690;
    --card: #f4f4f2;
    --orange: #e2661c;
    --black: #151515;
    --ink: #1e1e1e;
    --muted: #555;
  }
  * { box-sizing: border-box; margin: 0; padding: 0; }
  html, body {
    width: 1200px; height: 668px; overflow: hidden;
    background: var(--backdrop);
    font-family: "Open Sans", Arial, sans-serif;
  }
  .canvas {
    position: relative; width: 1200px; height: 668px;
    display: flex; align-items: center; justify-content: center; gap: 50px;
  }
  .card {
    position: relative; width: 525px; height: 300px;
    background: var(--card); overflow: hidden;
    box-shadow: 0 10px 24px rgba(0,0,0,.22);
  }
  .card__shapes { position: absolute; inset: 0; width: 100%; height: 100%; }
  .shape--orange { fill: var(--orange); }
  .shape--black { fill: var(--black); }

  .brand {
    display: flex; align-items: center; gap: 10px;
    color: var(--ink); font-weight: 700; line-height: 1.1;
  }
  .brand__mark { width: 18px; height: 18px; background: var(--orange); flex: none; }
  .brand__name { font-size: 20px; letter-spacing: .3px; }
  .brand__name small { display: block; font-size: 11px; letter-spacing: 1px; text-transform: uppercase; }

  .front-block {
    position: absolute; left: 150px; top: 50%; transform: translateY(-50%);
    display: flex; flex-direction: column; gap: 12px;
  }
  .card--front .brand__name { font-size: 24px; }
  .card--front .brand__name small { font-size: 12.5px; }
  .slogan {
    padding-left: 28px; font-size: 12.5px; font-weight: 600;
    color: var(--orange); letter-spacing: .4px;
  }

  .card--back .brand { position: absolute; left: 70px; top: 42px; }

  .contact { position: absolute; left: 232px; top: 118px; color: var(--ink); }
  .contact__name { font-size: 21px; font-weight: 700; line-height: 1.1; }
  .contact__role { font-size: 11px; color: var(--orange); margin-bottom: 12px; }
  .contact__list { list-style: none; font-size: 13px; line-height: 1.45; }
  .contact__list li { display: flex; align-items: center; gap: 7px; }
  .contact__list svg { width: 11px; height: 11px; fill: var(--orange); flex: none; }
  .contact__list .no-icon { padding-left: 18px; }

  .services {
    position: absolute; left: 20px; top: 254px; width: 280px;
    font-size: 10.5px; line-height: 1.4; font-weight: 600; color: var(--muted);
  }
</style>
</head>
<body>
<main class="canvas">

  <section class="card card--front" aria-label="Business card front">
    <svg class="card__shapes" viewBox="0 0 525 300" preserveAspectRatio="none" aria-hidden="true">
      <polygon class="shape--orange" points="0,0 80,0 120,120 0,230"/>
      <polygon class="shape--black" points="525,70 525,300 420,300 395,215"/>
    </svg>
    <div class="front-block">
      <div class="brand">
        <span class="brand__mark"></span>
        <span class="brand__name">Kestrel Hollow<small>Construction &amp; Maintenance</small></span>
      </div>
      <p class="slogan">Let Quality Meet Your Budget</p>
    </div>
  </section>

  <section class="card card--back" aria-label="Business card back">
    <svg class="card__shapes" viewBox="0 0 525 300" preserveAspectRatio="none" aria-hidden="true">
      <polygon class="shape--orange" points="0,70 55,100 175,245 0,245"/>
      <polygon class="shape--black" points="160,225 190,245 175,245"/>
      <polygon class="shape--orange" points="300,300 525,300 525,250 330,262"/>
    </svg>
    <div class="brand">
      <span class="brand__mark"></span>
      <span class="brand__name">Kestrel Hollow<small>Construction &amp; Maintenance</small></span>
    </div>
    <div class="contact">
      <p class="contact__name">Doran Pellick</p>
      <p class="contact__role">Managing Director</p>
      <ul class="contact__list">
        <li><svg viewBox="0 0 10 10"><path d="M2 0h3l1 3-1.5 1a5 5 0 0 0 1.5 1.5L7 4l3 1v3c0 1-1 2-2 2A8 8 0 0 1 0 2c0-1 1-2 2-2z"/></svg>0438 715 362</li>
        <li><svg viewBox="0 0 10 10"><path d="M0 2h10v6H0zM1 3l4 3 4-3z"/></svg>kestrelhollowbuild@mailpost.example</li>
        <li><svg viewBox="0 0 10 10"><path d="M5 0l5 5H8.5v5h-7V5H0z"/></svg>Perth, WA, Australia</li>
        <li class="no-icon">Building Registration BC584317</li>
      </ul>
    </div>
    <p class="services">New Homes · Medical Centres · Mixed Use<br>Renovations · Maintenance</p>
  </section>

</main>
</body>
</html>
```